New Template, new corporate image Datavista 2022

New template designs for google slides or PowerPoint. Match to new corporate image. The new website www.datavista-mx.example Needs to match our new version. Technology and Artificial Intelligence elements to reflect our type of work.
We are adding old version of template and will send elements for the new corporate images.
Please consider our website as the main corporate image.
Our templates are being used on customer presentations, webminars, internal work only.
We have our main name of company Datavista. Datavista has to be in all the templates.
Secondary logo or branded service is: Quorvitar.

Target Market(s)

Industrial users. Asset managers. Corporate visitors and customers.

Industry/Entity Type

Automotive. Chemical. Food and Beverage. Manufacturing

Font styles to use
Other font styles liked:
• GE INSPIRA. RALEWAY

Colors
0054AA
0677BA
7BADD7
CADEEF
E8F1F8

Requirements
Must have
• Match to our elements on the new image. Use Brain Icons. Chips icons to connect equipments with software and control. Innovation.
Nice to have
• Unique images, machine images. Connecting machines and data elements. Template version for google slides. Image for industrial software for control equipment and saving money to manufacturers. Segments: Automotive, Chemical, Food and Beverages, Mining and pharmaceutical, Energy Management
Should not have
• old elements. not to much images of medical devices. Do not seems like a hospital.

```html
<!DOCTYPE html>
<html lang="en">
<head>
<meta charset="utf-8">
<title>Datavista – Slide Template Collection</title>
<link href="https://fonts.googleapis.com/css2?family=Saira+Semi+Condensed:wght@500;600&family=Open+Sans:wght@400;600&display=swap" rel="stylesheet">
<style>
  :root{
    --navy:#0054AA;
    --blue:#1877C2;
    --sky:#7BADD7;
    --mist:#CADEEF;
    --ice:#EEF5FB;
    --ink:#111418;
    --board:#F1F2F4;
    --white:#FFFFFF;
    --deep:#07182F;
  }
  *{margin:0;padding:0;box-sizing:border-box}
  html,body{width:718px;height:1200px;overflow:hidden;background:var(--board)}
  body{position:relative;font-family:"Open Sans",sans-serif;color:var(--ink)}
  .sprite{position:absolute;width:0;height:0;overflow:hidden}

  .slide{position:absolute;width:255px;height:143px;overflow:hidden;background:var(--white);box-shadow:0 2px 4px rgba(0,0,0,.22)}
  .col-left{left:76px}.col-right{left:373px}
  .row-1{top:72px}.row-2{top:255px}.row-3{top:439px}.row-4{top:622px}.row-5{top:805px}.row-6{top:988px}

  .abs{position:absolute}
  .header{position:absolute;left:0;top:0;right:0;height:24px;background:var(--white);z-index:3}
  .title{position:absolute;left:16px;top:4px;font-family:"Saira Semi Condensed",sans-serif;font-weight:500;font-size:12.5px;letter-spacing:.2px;color:var(--ink);white-space:nowrap}
  .brand{position:absolute;right:13px;top:8px;font-family:"Saira Semi Condensed",sans-serif;font-weight:500;font-size:7px;color:var(--blue);letter-spacing:.3px}
  .footer{position:absolute;left:0;right:0;bottom:0;height:7px;background:var(--blue);z-index:3}
  .url{position:absolute;left:16px;bottom:2px;font-size:2.4px;color:var(--white);z-index:4}
  .page{position:absolute;font-size:2.4px;color:#9aa4b0}

  .heading{font-family:"Saira Semi Condensed",sans-serif;font-weight:600;font-size:5.6px;color:var(--ink);white-space:nowrap}
  .body{font-size:3px;line-height:1.3;color:var(--ink)}
  .body.light{color:var(--white)}
  .bullets{list-style:none}
  .bullets li{position:relative;padding-left:6px}
  .bullets li::before{content:"•";position:absolute;left:0}

  .photo{position:absolute}

  .icon-ring{position:absolute;width:17px;height:17px;border-radius:50%;border:2.5px solid var(--blue);background:var(--white);display:flex;align-items:center;justify-content:center}
  .icon-ring svg{width:55%;height:55%;color:var(--blue)}
  .icon-label{position:absolute;font-size:2.6px;width:30px;text-align:center}

  /* cover */
  .cover{background:var(--deep)}
  .cover .photo{inset:0;background:
    radial-gradient(ellipse 22% 30% at 74% 30%,rgba(90,180,255,.85) 0,rgba(30,110,200,.55) 45%,rgba(7,27,54,0) 100%),
    radial-gradient(ellipse 40% 22% at 72% 80%,rgba(20,90,170,.55) 0,rgba(7,27,54,0) 100%),
    linear-gradient(90deg,#050d1a 0,#081a33 45%,#0a2748 100%)}
  .cover-brand{position:absolute;left:19px;top:54px;font-family:"Saira Semi Condensed",sans-serif;font-weight:500;font-size:13px;color:var(--sky)}
  .cover-tag{position:absolute;left:18px;top:83px;width:88px;font-size:2.6px;line-height:1.3;color:var(--white)}

  /* ring */
  .ring-stage{position:absolute;left:0;top:24px;right:0;bottom:7px;background:var(--ice)}
  .pill{position:absolute;height:10px;width:74px;background:var(--blue);border-radius:2px;box-shadow:0 1px 2px rgba(0,0,0,.25);font-size:2.4px;color:var(--white);line-height:10px;padding:0 3px;white-space:nowrap}
  .pill.right{text-align:right}

  /* agenda */
  .agenda-panel{position:absolute;left:0;top:24px;width:104px;bottom:0;background:var(--blue)}
  .agenda-line{position:absolute;left:86px;top:0;bottom:0;width:1.2px;background:var(--white)}
  .agenda-item{position:absolute;right:26px;width:56px;text-align:right;color:var(--white)}
  .agenda-item h3{font-family:"Saira Semi Condensed",sans-serif;font-weight:600;font-size:4.6px;margin-bottom:2px}
  .agenda-item p{font-size:2.2px;line-height:1.3}
  .agenda-dot{position:absolute;left:80px;width:13px;height:13px;border-radius:50%;background:var(--blue);border:1px solid var(--white);color:var(--white);font-size:4px;text-align:center;line-height:11px}

  /* divider */
  .divider{background:#0b1c2e}
  .divider .photo{inset:0;background:
    radial-gradient(ellipse 30% 40% at 70% 30%,rgba(120,150,160,.55) 0,rgba(20,40,55,0) 100%),
    radial-gradient(ellipse 25% 35% at 18% 70%,rgba(150,110,40,.45) 0,rgba(20,40,55,0) 100%),
    linear-gradient(120deg,#121f2b 0,#1c3642 50%,#0e2131 100%)}
  .divider-band{position:absolute;left:0;right:0;bottom:0;height:34px;background:var(--blue)}
  .divider-title{position:absolute;left:17px;bottom:9px;font-family:"Saira Semi Condensed",sans-serif;font-weight:500;font-size:11.5px;color:var(--white)}
  .divider-brand{position:absolute;left:163px;top:60px;font-family:"Saira Semi Condensed",sans-serif;font-weight:500;font-size:10.5px;color:var(--white)}
  .divider-text{position:absolute;left:155px;bottom:13px;width:90px;font-size:3.4px;line-height:1.3;color:var(--white)}

  /* AR */
  .ar-panel{position:absolute;left:0;top:24px;width:242px;bottom:0;background:var(--blue)}
  .card{position:absolute;top:87px;width:34px;height:56px;background:var(--white);border-radius:17px 17px 0 0}
  .card .icon-ring{left:2px;top:2px;width:30px;height:30px}
  .card p{position:absolute;left:4px;top:38px;width:26px;font-size:1.9px;line-height:1.3;color:#8a96a3}
  .card i{position:absolute;left:8px;bottom:2px;width:18px;height:.8px;background:var(--blue)}

  .split-blue{position:absolute;left:0;top:24px;width:128px;bottom:0;background:var(--blue)}
  .split-ice{position:absolute;left:128px;top:24px;right:0;bottom:0;background:var(--ice)}

  .num-bar{position:absolute;left:20px;height:6px;width:58px;background:var(--blue);border-radius:3px}
  .num-bar span{position:absolute;left:-1px;top:-1px;width:8px;height:8px;border-radius:50%;border:.8px solid var(--white);background:var(--navy);color:var(--white);font-size:3px;text-align:center;line-height:6.5px}

  .hub-icon{position:absolute;width:12px;height:12px;border-radius:50%;border:1.1px solid var(--white);background:var(--blue);display:flex;align-items:center;justify-content:center}
  .hub-icon svg{width:60%;height:60%;color:var(--white)}

  table.data{position:absolute;left:42px;top:45px;width:170px;border-collapse:collapse;font-size:2.4px;color:#8a96a3}
  table.data th{background:var(--blue);height:6px;border-right:.5px solid var(--white)}
  table.data td{height:7.8px;border-right:.5px solid var(--white);background:#E4ECF5}
  table.data tr:nth-child(odd) td{background:#C8D8EC}
  table.data td.n{width:8px;background:var(--white)!important;text-align:center}
</style>
</head>
<body>

<svg class="sprite" aria-hidden="true">
  <symbol id="i-chip" viewBox="0 0 24 24"><g fill="none" stroke="currentColor" stroke-width="2"><rect x="6" y="6" width="12" height="12" rx="1"/><rect x="9.5" y="9.5" width="5" height="5"/><path d="M9 2v4M15 2v4M9 18v4M15 18v4M2 9h4M2 15h4M18 9h4M18 15h4"/></g></symbol>
  <symbol id="i-cube" viewBox="0 0 24 24"><g fill="none" stroke="currentColor" stroke-width="2" stroke-linejoin="round"><path d="M12 2l9 5v10l-9 5-9-5V7z"/><path d="M3 7l9 5 9-5M12 12v10"/></g></symbol>
  <symbol id="i-globe" viewBox="0 0 24 24"><g fill="none" stroke="currentColor" stroke-width="2"><circle cx="12" cy="12" r="9"/><path d="M3 12h18M12 3c3 3 3 15 0 18M12 3c-3 3-3 15 0 18"/></g></symbol>
  <symbol id="i-nodes" viewBox="0 0 24 24"><g fill="none" stroke="currentColor" stroke-width="2"><circle cx="12" cy="12" r="3"/><circle cx="5" cy="5" r="2"/><circle cx="19" cy="5" r="2"/><circle cx="5" cy="19" r="2"/><circle cx="19" cy="19" r="2"/><path d="M7 7l3 3M17 7l-3 3M7 17l3-3M17 17l-3-3"/></g></symbol>
  <symbol id="i-bolt" viewBox="0 0 24 24"><path d="M13 2L4 14h7l-1 8 9-12h-7z" fill="none" stroke="currentColor" stroke-width="2" stroke-linejoin="round"/></symbol>
  <symbol id="i-arrow" viewBox="0 0 24 24"><path d="M5 19L19 5M9 5h10v10" fill="none" stroke="currentColor" stroke-width="2" stroke-linecap="round"/></symbol>
  <symbol id="i-phone" viewBox="0 0 24 24"><g fill="none" stroke="currentColor" stroke-width="2"><rect x="7" y="2" width="10" height="20" rx="2"/><path d="M11 18h2"/></g></symbol>
</svg>

<!-- Cover -->
<section class="slide cover col-left row-1">
  <div class="photo" role="img" aria-label="Glowing blue digital brain above a circuit board on a dark background"></div>
  <div class="cover-brand">Datavista</div>
  <p class="cover-tag">We are specialists in automation, process control, information technologies, development and consulting for quality, efficiency</p>
</section>

<!-- Ring overview -->
<section class="slide col-right row-1">
  <div class="header"><h2 class="title">Digital Operations Center</h2><span class="brand">Datavista</span></div>
  <div class="ring-stage"></div>
  <div class="pill" style="left:22px;top:56px">There are high security and production risks.</div>
  <div class="pill" style="left:22px;top:72px">There are high security and production risks.</div>
  <div class="pill" style="left:22px;top:89px">There are high security and production risks.</div>
  <div class="pill right" style="left:160px;top:56px">There are high security and production risks.</div>
  <div class="pill right" style="left:160px;top:72px">There are high security and production risks.</div>
  <div class="pill right" style="left:160px;top:89px">There are high security and production risks.</div>
  <svg class="abs" style="left:85px;top:33px" width="92" height="92" viewBox="0 0 92 92">
    <circle cx="46" cy="46" r="44" fill="#fff"/>
    <circle cx="46" cy="46" r="32" fill="#fff" stroke="#1877C2" stroke-width="9"/>
  </svg>
  <span class="abs" style="left:116px;top:76px;font-family:'Saira Semi Condensed',sans-serif;font-weight:500;font-size:5px;color:var(--blue)">Datavista</span>
  <div class="footer"></div><span class="url">www.datavista-mx.example</span>
</section>

<!-- Agenda -->
<section class="slide col-left row-2">
  <div class="header"><h2 class="title">Agenda</h2><span class="brand">Datavista</span></div>
  <div class="agenda-panel">
    <div class="agenda-line"></div>
    <div class="agenda-item" style="top:20px"><h3>Agenda</h3><p>• For complex production systems that require autonomy, control of PLC equipment, PAC.</p></div>
    <div class="agenda-item" style="top:53px"><h3>Agenda</h3><p>• For complex production systems that require autonomy, control of PLC equipment, PAC.</p></div>
    <div class="agenda-item" style="top:87px"><h3>Agenda</h3><p>• For complex production systems that require autonomy, control of PLC equipment, PAC.</p></div>
    <div class="agenda-dot" style="top:20px">1</div>
    <div class="agenda-dot" style="top:53px">2</div>
    <div class="agenda-dot" style="top:87px">3</div>
  </div>
  <div class="photo" style="left:104px;top:24px;right:0;bottom:0;background:
    radial-gradient(ellipse 40% 45% at 25% 20%,rgba(235,160,60,.9) 0,rgba(235,160,60,0) 100%),
    radial-gradient(ellipse 35% 35% at 80% 40%,rgba(70,90,110,.6) 0,rgba(70,90,110,0) 100%),
    linear-gradient(160deg,#d9b27a 0,#e8e2d8 40%,#b9c6d2 70%,#6e8298 100%)" role="img" aria-label="Person writing in a notebook with digital network graphics overlay"></div>
</section>

<!-- Overview with icons -->
<section class="slide col-right row-2">
  <div class="header"><h2 class="title">Digital Operations Center</h2><span class="brand">Datavista</span></div>
  <div class="photo" style="left:105px;top:24px;right:0;bottom:7px;background:
    radial-gradient(ellipse 25% 45% at 22% 50%,rgba(170,205,205,1) 0,rgba(170,205,205,0) 100%),
    radial-gradient(ellipse 30% 35% at 85% 85%,rgba(210,130,40,.9) 0,rgba(210,130,40,0) 100%),
    radial-gradient(ellipse 18% 25% at 45% 35%,rgba(60,210,220,.7) 0,rgba(60,210,220,0) 100%),
    linear-gradient(90deg,#ffffff 0,#6d9aa2 28%,#244654 55%,#1b303c 100%)" role="img" aria-label="Humanoid robot head with holographic data interface and industrial robot arm"></div>
  <h3 class="heading abs" style="left:21px;top:49px;font-size:4.8px">Digital Operations Center</h3>
  <p class="body abs" style="left:21px;top:62px;width:78px;font-size:2.8px">For complex production systems that require autonomy, control of PLC equipment, PAC. Networks, actuators and distributed control systems, a digital command center is the best alternative to continue operating production plants.</p>
  <div class="icon-ring" style="left:18px;top:96px"><svg><use href="#i-globe"/></svg></div>
  <div class="icon-ring" style="left:46px;top:96px"><svg><use href="#i-cube"/></svg></div>
  <div class="icon-ring" style="left:74px;top:96px"><svg><use href="#i-chip"/></svg></div>
  <span class="icon-label" style="left:12px;top:116px">Network</span>
  <span class="icon-label" style="left:40px;top:116px">Networks</span>
  <span class="icon-label" style="left:68px;top:116px">Networks</span>
  <div class="footer"></div><span class="url">www.datavista-mx.example</span>
</section>

<!-- Section divider -->
<section class="slide divider col-left row-3">
  <div class="photo" role="img" aria-label="Person wearing a VR headset among industrial robot arms"></div>
  <svg class="abs" style="left:0;top:0" width="255" height="110" viewBox="0 0 255 110">
    <polygon points="0,0 80,0 150,68 40,110 0,110 0,100 42,110 120,68 60,0 0,0" fill="#1877C2" opacity=".9"/>
  </svg>
  <span class="divider-brand">Datavista</span>
  <div class="divider-band"></div>
  <span class="divider-title">Datavista</span>
  <p class="divider-text">Complex production systems that require autonomy, control of PLC equipment, PAC,</p>
</section>

<!-- Image left, text right -->
<section class="slide col-right row-3">
  <span class="brand">Datavista</span>
  <div class="photo" style="left:0;top:38px;width:145px;bottom:0;background:
    radial-gradient(ellipse 28% 50% at 62% 45%,rgba(240,170,60,.95) 0,rgba(240,170,60,0) 100%),
    linear-gradient(90deg,#8ea4ba 0,#cfd9e3 35%,#f2e6d4 60%,#ffffff 100%)" role="img" aria-label="Engineer with VR headset reaching toward a robotic arm amid network lines"></div>
  <h3 class="heading abs" style="left:157px;top:73px">Digital Operations Center</h3>
  <ul class="body bullets abs" style="left:150px;top:97px;width:95px;font-size:2.6px">
    <li>For complex production systems that require autonomy, control of PLC equipment, PAC.</li>
    <li>Networks, actuators and distributed control systems, a digital command center is the best alternative to continue operating production plants.</li>
  </ul>
  <span class="page" style="right:15px;bottom:5px">6</span>
</section>

<!-- Augmented reality -->
<section class="slide col-left row-4">
  <div class="header"><h2 class="title" style="left:18px">Augmented Reality</h2><span class="brand">Datavista</span></div>
  <div class="ar-panel"></div>
  <svg class="abs" style="left:160px;top:40px" width="82" height="100" viewBox="0 0 82 100">
    <circle cx="50" cy="50" r="48" fill="none" stroke="#2a88cf" stroke-width="6"/>
    <circle cx="50" cy="50" r="41" fill="#fff"/>
  </svg>
  <div class="photo" style="left:108px;top:32px;width:104px;height:86px;background:radial-gradient(ellipse 45% 45% at 50% 48%,rgba(232,237,242,.95) 0,rgba(160,172,186,.8) 50%,rgba(24,119,194,0) 100%)" role="img" aria-label="Floating white humanoid robot"></div>
  <h3 class="heading abs" style="left:20px;top:39px;color:#fff;font-size:4.8px">Digital Operations Center</h3>
  <p class="body light abs" style="left:19px;top:52px;width:70px;font-size:2.5px">For complex production systems that require autonomy, control of PLC equipment, PAC, Networks, actuators and distributed control systems, a digital command center is the best alternative to continue operating production plants.</p>
  <div class="card" style="left:8px"><div class="icon-ring"><svg><use href="#i-globe"/></svg></div><p>When a plant has several PLC, PAC and controller brands.</p><i></i></div>
  <div class="card" style="left:47px"><div class="icon-ring"><svg><use href="#i-cube"/></svg></div><p>When production assets have a high maintenance cost.</p><i></i></div>
  <div class="card" style="left:86px"><div class="icon-ring"><svg><use href="#i-chip"/></svg></div><p>In multiple industrial platforms needing one unified command.</p><i></i></div>
  <span class="page" style="left:238px;bottom:6px;color:#cfe0f0">10</span>
</section>

<!-- Text left, image right -->
<section class="slide col-right row-4">
  <div class="header"><h2 class="title">Digital Operations Center</h2><span class="brand">Datavista</span></div>
  <div class="abs" style="left:0;top:24px;width:127px;bottom:0;background:var(--ice)"></div>
  <div class="photo" style="left:127px;top:24px;right:0;bottom:7px;background:
    radial-gradient(ellipse 28% 25% at 55% 30%,rgba(170,215,250,.95) 0,rgba(170,215,250,0) 100%),
    radial-gradient(ellipse 40% 18% at 55% 62%,rgba(110,170,230,.6) 0,rgba(110,170,230,0) 100%),
    linear-gradient(180deg,#123d78 0,#0d2c5e 60%,#0a1f44 100%)" role="img" aria-label="Hand holding a tablet with a glowing cloud upload symbol over a city"></div>
  <h3 class="heading abs" style="left:23px;top:52px">Digital Operations Center</h3>
  <ul class="body bullets abs" style="left:16px;top:74px;width:95px">
    <li>For complex production systems that require autonomy, control of PLC equipment, PAC,</li>
    <li>Networks, actuators and distributed control systems, a digital command center is the best alternative to continue operating production plants.</li>
  </ul>
  <div class="footer"></div><span class="url">www.datavista-mx.example</span>
</section>

<!-- Org chart -->
<section class="slide col-left row-5">
  <div class="header"><h2 class="title">Digital Operations Centerc</h2><span class="brand">Datavista</span></div>
  <div class="split-blue"></div>
  <div class="split-ice"></div>
  <p class="body light abs" style="left:15px;top:45px;width:80px;font-size:4px">When production assets have a high maintenance cost.</p>
  <svg class="abs" style="left:19px;top:71px" width="92" height="46" viewBox="0 0 92 46">
    <rect x="19" y="0" width="54" height="8" fill="#fff"/>
    <path d="M46 8V14M15 14H77M15 14V21M46 14V21M77 14V21" stroke="#fff" stroke-width="1" fill="none"/>
    <rect x="2" y="21" width="27" height="8" fill="#fff"/><rect x="33" y="21" width="27" height="8" fill="#fff"/><rect x="64" y="21" width="27" height="8" fill="#fff"/>
    <rect x="2" y="34" width="27" height="8" fill="#fff"/><rect x="33" y="34" width="27" height="8" fill="#fff"/><rect x="64" y="34" width="27" height="8" fill="#fff"/>
  </svg>
  <div class="photo" style="left:163px;top:42px;width:56px;height:72px;background:radial-gradient(ellipse 42% 46% at 50% 45%,#ffffff 0,#d6dde4 55%,rgba(238,245,251,0) 100%)" role="img" aria-label="Small white service robot mascot"></div>
  <span class="url" style="left:16px">www.datavista-mx.example</span>
  <span class="page" style="right:16px;bottom:5px">9</span>
</section>

<!-- Numbered list over image -->
<section class="slide col-right row-5">
  <div class="header"><h2 class="title">Digital Operations Centerc</h2><span class="brand">Datavista</span></div>
  <div class="photo" style="left:0;top:24px;right:0;bottom:7px;background:
    radial-gradient(ellipse 15% 15% at 22% 12%,rgba(220,150,40,.85) 0,rgba(220,150,40,0) 100%),
    radial-gradient(ellipse 20% 25% at 40% 70%,rgba(180,120,60,.5) 0,rgba(180,120,60,0) 100%),
    linear-gradient(90deg,#16243a 0,#24374d 35%,#1d4c7e 60%,#2e6aa6 100%)" role="img" aria-label="Engineer in hard hat with industrial robots and holographic dashboards"></div>
  <div class="abs" style="left:127px;top:24px;right:0;bottom:7px;background:rgba(24,119,194,.45)"></div>
  <p class="body light abs" style="left:18px;top:50px;width:100px;font-size:4px">For complex production systems that require autonomy, control of PLC equipment, PAC, plants.</p>
  <h3 class="heading abs" style="left:18px;top:80px;color:#fff;font-size:4.4px">Digital Operations Center</h3>
  <div class="num-bar" style="top:96px"><span>1</span></div>
  <div class="num-bar" style="top:107px"><span>2</span></div>
  <div class="num-bar" style="top:118px"><span>3</span></div>
  <h3 class="heading abs" style="left:142px;top:64px;color:#fff;font-size:6.4px">Digital Operations Center</h3>
  <p class="body light abs" style="left:142px;top:81px;width:100px;font-size:4px">For complex production systems that require autonomy, control of PLC equipment, PAC, Networks, actuators and distributed control systems, a digital command center is the best alternative to continue operating production plants.</p>
  <div class="footer"></div><span class="url">www.datavista-mx.example</span>
</section>

<!-- Hub diagram -->
<section class="slide col-left row-6">
  <div class="header"><h2 class="title">Digital Operations Centerc</h2><span class="brand">Datavista</span></div>
  <div class="abs" style="left:0;top:24px;width:127px;bottom:0;background:var(--blue)"></div>
  <div class="abs" style="left:127px;top:24px;right:0;bottom:0;background:var(--ice)"></div>
  <svg class="abs" style="left:14px;top:42px" width="100" height="70" viewBox="0 0 100 70">
    <g fill="none" stroke="#fff" stroke-width="1.1">
      <path d="M2 60V25H28M98 60V25H72M18 60V38H35M82 60V38H65M50 48V60"/>
    </g>
    <circle cx="50" cy="24" r="24" fill="#fff"/>
    <circle cx="50" cy="24" r="21.5" fill="none" stroke="#1877C2" stroke-width="1.5"/>
  </svg>
  <div class="hub-icon" style="left:13px;top:98px"><svg><use href="#i-arrow"/></svg></div>
  <div class="hub-icon" style="left:30px;top:98px"><svg><use href="#i-chip"/></svg></div>
  <div class="hub-icon" style="left:47px;top:98px"><svg><use href="#i-phone"/></svg></div>
  <div class="hub-icon" style="left:64px;top:98px"><svg><use href="#i-nodes"/></svg></div>
  <div class="hub-icon" style="left:81px;top:98px"><svg><use href="#i-bolt"/></svg></div>
  <span class="abs" style="left:52px;top:63px;font-family:'Saira Semi Condensed',sans-serif;font-weight:500;font-size:5px;color:var(--blue)">Datavista</span>
  <h3 class="heading abs" style="left:140px;top:62px;font-size:4.4px">Digital Operations Center</h3>
  <ul class="body bullets abs" style="left:135px;top:77px;width:105px;font-size:3.8px">
    <li>For complex production systems that require autonomy, control of PLC equipment, PAC,</li>
    <li>Networks, actuators and distributed control systems, a digital command center is the best alternative to continue operating production plants.</li>
  </ul>
  <span class="url">www.datavista-mx.example</span>
  <span class="page" style="right:15px;bottom:5px">11</span>
</section>

<!-- Table -->
<section class="slide col-right row-6">
  <div class="header"><h2 class="title">Digital Operations Centerc</h2><span class="brand">Datavista</span></div>
  <div class="abs" style="left:0;top:24px;right:0;bottom:0;background:var(--ice)"></div>
  <table class="data">
    <tr><th style="width:8px"></th><th></th><th></th><th></th><th></th><th></th></tr>
    <tr><td class="n">1</td><td></td><td></td><td></td><td></td><td></td></tr>
    <tr><td class="n">2</td><td></td><td></td><td></td><td></td><td></td></tr>
    <tr><td class="n">3</td><td></td><td></td><td></td><td></td><td></td></tr>
    <tr><td class="n">4</td><td></td><td></td><td></td><td></td><td></td></tr>
    <tr><td class="n">5</td><td></td><td></td><td></td><td></td><td></td></tr>
    <tr><td class="n">6</td><td></td><td></td><td></td><td></td><td></td></tr>
    <tr><td class="n">7</td><td></td><td></td><td></td><td></td><td></td></tr>
  </table>
  <div class="footer"></div><span class="url">www.datavista-mx.example</span>
</section>

</body>
</html>
```